Business Card Design

Lintel Comms is a public relations consultancy service for the self build, home refurbishment and home improvement market.
It represents everything about 'home' so envisage logo featuring maybe roof pitch over the 'A' of Lintel. Colour/font undecided.

Industry/Entity Type

Home Improvement

Contact Information for Business Card

Fenella Coxworth
fenella@lintelcomms.co.uk
Telephone Direct: 0788 142 6597

```html
<!DOCTYPE html>
<html lang="en">
<head>
<meta charset="utf-8">
<title>Lintel Comms — Business Card</title>
<link rel="stylesheet" href="https://fonts.googleapis.com/css2?family=Montserrat:wght@700&family=Didact+Gothic&display=swap">
<style>
  :root {
    --orange: #f07a1a;
    --ink: #2b2b2b;
    --grey: #5a5a5a;
    --card: #ffffff;
    --backdrop: #e9e6e2;
  }
  * { margin: 0; padding: 0; box-sizing: border-box; }
  html, body { width: 1200px; height: 843px; overflow: hidden; }
  body {
    background: var(--backdrop);
    font-family: "Didact Gothic", "Century Gothic", sans-serif;
    display: flex;
    align-items: center;
    justify-content: center;
    gap: 60px;
  }
  .card {
    position: relative;
    width: 520px;
    height: 297px;
    background: var(--card);
    box-shadow: 0 6px 20px rgba(0,0,0,0.15);
    overflow: hidden;
  }
  .brand {
    position: absolute;
    display: flex;
    flex-direction: column;
    align-items: center;
  }
  .brand-name-row { display: flex; align-items: center; gap: 10px; }
  .brand-square { width: 16px; height: 16px; background: var(--orange); }
  .brand-name {
    font-family: "Montserrat", sans-serif;
    font-weight: 700;
    color: var(--ink);
    text-transform: uppercase;
    letter-spacing: 0.5px;
  }
  .brand-tag {
    font-family: "Montserrat", sans-serif;
    font-weight: 700;
    color: var(--ink);
    text-transform: uppercase;
    letter-spacing: 1px;
  }

  /* front */
  .card-front .brand { left: 0; right: 0; top: 104px; }
  .card-front .brand-name { font-size: 40px; }
  .card-front .brand-tag { font-size: 13px; margin-top: 4px; }
  .card-front .edge-right {
    position: absolute; right: 0; top: 0; bottom: 0; width: 8px; background: var(--orange);
  }

  /* back */
  .card-back .brand { left: 0; right: 0; top: 40px; }
  .card-back .brand-name { font-size: 30px; }
  .card-back .brand-tag { font-size: 10px; margin-top: 3px; }
  .contact {
    position: absolute; left: 22px; top: 124px;
    font-size: 13px; color: var(--grey); line-height: 1.9;
  }
  .contact .label { color: var(--orange); margin-right: 4px; }
  .divider {
    position: absolute; left: 22px; right: 22px; top: 196px; height: 1.5px; background: var(--orange);
  }
  .person {
    position: absolute; right: 26px; top: 174px; text-align: right;
  }
  .person-name { color: var(--orange); font-size: 18px; }
  .person-role { color: var(--ink); font-size: 12px; margin-top: 2px; }
  .band {
    position: absolute; left: 0; right: 0; bottom: 0; height: 40px; background: var(--orange);
  }
</style>
</head>
<body>
  <section class="card card-front" aria-label="Card front">
    <div class="brand">
      <div class="brand-name-row">
        <span class="brand-square"></span>
        <span class="brand-name">Lintel Comms</span>
      </div>
      <span class="brand-tag">Consultancy</span>
    </div>
    <div class="edge-right"></div>
  </section>

  <section class="card card-back" aria-label="Card back">
    <div class="brand">
      <div class="brand-name-row">
        <span class="brand-square"></span>
        <span class="brand-name">Lintel Comms</span>
      </div>
      <span class="brand-tag">Consultancy</span>
    </div>
    <div class="contact">
      <div><span class="label">Phone</span>0788 142 6597</div>
      <div><span class="label">Email</span>fenella@lintelcomms.co.uk</div>
    </div>
    <div class="divider"></div>
    <div class="person">
      <div class="person-name">Fenella Coxworth</div>
      <div class="person-role">Consultant</div>
    </div>
    <div class="band"></div>
  </section>
</body>
</html>
```